Tourism Marketing needing sleek, clear design for business card & proposal documents.

***Company background***
"Quiet Harbour" is a company specializing in tourism marketing and project management. We do international wholesale, event management as well as ongoing representation of tourism and hospitality companies.

***Target market***
We cater to tourism companies and hotel professionals.

***Task***
We would like to get a single sided business card designed (but will still consider two sided, we are open to any ideas you may have). The layout for this card should be modern and elegant. Currently we do not have a logo, but we would like our business name in a really simple typography for the business card (similar to Moonrise Palace's logo - www.moonrisepalace-example.com.au).We are after a design that is clear, strong enough to be recognised as Quiet Harbour that does not require any fancy design. Another option is a simple play on QH (Quiet Harbour) or simply have Quiet Harbour featured elsewhere on card more as a brand/logo.

Feel free to submit different fonts if you feel you have any other fonts/designs that may be suitable for this card other than sans serifs. Should this project be successful, we will be considering several other projects for business proposal templates and eventually a website design.

The information that needs to go on the card are as follows:

Marta Holloway
Director
Quiet Harbour
Tourism Marketing & Representation
87 Wendover Parade
Prahran, Victoria, 3181 Australia
T +61 498203617 E marta@quietharbour-example.com.au

***Look and feel***
We'd like the business card design to express the following:
Modern, sleek, elegant, simple, discreet, quality, subtle, professional, creative, innovation

In terms of typography, we like something really simple and blocky (similar font to Moonrise Palace's logo - www.moonrisepalace-example.com.au)

***Colour scheme***
Shades of grey and dark teal

***Note***
Although our main target market are professionals, we would like the business card design to be versatile enough to be used outside of the tourism industry and need to appeal to different markets.

I do not have existing logo. Was hoping for a design that may be clear, strong enough not to require one. Other option is a simple play on QH (Quiet Harbour) or simply have Quiet Harbour featured elsewhere on card more as a brand/logo.

Marta Holloway
Director
Quiet Harbour Pty Ltd 
87 Wendover Parade
T +61 498203617  E  marta@quietharbour-example.com.au

Thank you for designs so far. Many have used a mauve colour which matches our company profile. This is not necessary, as that is just a draft and will be completely redesigned, so dont  feel you need to incorporate the mauve.

My colour preferences are for a white or grey background, and I like fonts in dark teals, grey or other sophisticated but modern colours. feel free to submit different fonts if you you have other fonts you thing would be suitable for this card, along with sans serifs. Should this project be successful, we will be considering several others for business proposal templates and eventually website. 

Target Market(s)

International Hospitality Senior Executives, Directors of International Tourism Companies, Directors of Tourism Bodies Internationally, local Tourism

Industry/Entity Type

Hospitality

Requirements
Should not have
• must not have bright garish colour, swirly patterns or anything that dates too much.

```html
<!DOCTYPE html>
<html lang="en">
<head>
<meta charset="utf-8">
<title>Quiet Harbour — Business Card</title>
<link rel="stylesheet" href="https://fonts.googleapis.com/css2?family=Montserrat:wght@400;500;700&family=Questrial&display=swap">
<style>
  :root {
    --page: #ffffff;
    --card: #e6e6e7;
    --ink: #6a6a6c;
    --ink-soft: #9a9a9c;
    --teal: #1e8f8c;
    --rule: #8d8d8f;
    --shadow: rgba(0, 0, 0, 0.18);
  }
  * { margin: 0; padding: 0; box-sizing: border-box; }
  html, body {
    width: 1200px;
    height: 1200px;
    overflow: hidden;
    background: var(--page);
  }
  .canvas {
    position: relative;
    width: 1200px;
    height: 1200px;
  }
  .card {
    position: absolute;
    left: 270px;
    width: 690px;
    height: 420px;
    background: var(--card);
    box-shadow: 6px 8px 10px var(--shadow);
    text-align: center;
    color: var(--ink);
  }
  .card--front { top: 112px; }
  .card--back { top: 625px; }

  .wordmark {
    position: absolute;
    left: 0; right: 0;
    top: 172px;
    font-family: "Montserrat", sans-serif;
    font-weight: 500;
    font-size: 27px;
    line-height: 52px;
    letter-spacing: 0.3em;
    padding-left: 0.3em;
    color: var(--ink);
  }
  .tagline {
    position: absolute;
    left: 0; right: 0;
    top: 363px;
    font-family: "Questrial", sans-serif;
    font-size: 19px;
    letter-spacing: 0.1em;
    color: var(--ink-soft);
  }

  .person {
    position: absolute;
    left: 0; right: 0;
    top: 180px;
  }
  .person__name {
    font-family: "Montserrat", sans-serif;
    font-weight: 700;
    font-size: 19px;
    letter-spacing: 0.12em;
    color: var(--ink);
  }
  .person__role {
    margin-top: 6px;
    font-family: "Questrial", sans-serif;
    font-size: 19px;
    letter-spacing: 0.1em;
    color: var(--teal);
  }
  .divider {
    position: absolute;
    left: 253px;
    top: 270px;
    width: 184px;
    height: 1px;
    background: var(--rule);
  }
  .contact {
    position: absolute;
    left: 0; right: 0;
    top: 314px;
    font-family: "Questrial", sans-serif;
    font-style: normal;
    font-size: 18px;
    line-height: 24px;
    letter-spacing: 0.08em;
    color: var(--ink-soft);
  }
  .contact__line--compact {
    font-size: 16px;
    letter-spacing: 0.05em;
  }
  .contact__label {
    color: var(--teal);
    font-weight: 700;
    font-family: "Montserrat", sans-serif;
    font-size: 12px;
    margin-right: 6px;
  }
  .contact__gap { display: inline-block; width: 14px; }
</style>
</head>
<body>
<main class="canvas">
  <section class="card card--front" aria-label="Card front">
    <div class="wordmark">QUIET<br>HARBOUR</div>
    <p class="tagline">TOURISM MARKETING &amp; REPRESENTATION</p>
  </section>

  <section class="card card--back" aria-label="Card back">
    <div class="person">
      <p class="person__name">MARTA HOLLOWAY</p>
      <p class="person__role">DIRECTOR</p>
    </div>
    <div class="divider"></div>
    <address class="contact">
      <p>87 WENDOVER PARADE</p>
      <p>ELMSTEAD VIC 3187 AUSTRALIA</p>
      <p class="contact__line--compact"><span class="contact__label">T</span>+61 498 203 617<span class="contact__gap"></span><span class="contact__label">E</span>MARTA@QUIETHARBOUR-EXAMPLE.COM.AU</p>
    </address>
  </section>
</main>
</body>
</html>
```